Can you design a business card design? Looking for something unique and different. Can you design a business card design? Looking for something unique and different.Can you design a business card design? Looking for something unique and different.Can you design a business card design? Looking for something unique and different.Can you design a business card design? Looking for something unique and different.Can you design a business card design? Looking for something unique and different.

Industry/Entity Type

Business

Contact Information for Business Card

Can you design a business card design? Looking for something unique and different.

Font styles to use
Serif

```html
<!DOCTYPE html>
<html lang="en">
<head>
<meta charset="utf-8">
<title>Larkvale Business Card</title>
<link rel="stylesheet" href="https://fonts.googleapis.com/css2?family=Lato:wght@400;700&family=Oswald:wght@600&display=swap">
<style>
  :root {
    --page-bg: #ece9f0;
    --card-white: #f5f5f6;
    --panel-dark: #48484b;
    --brand-purple: #8f6bb3;
    --text-light: #ffffff;
    --text-muted: #e2e2e4;
  }
  * { box-sizing: border-box; margin: 0; padding: 0; }
  html, body {
    width: 1200px;
    height: 800px;
    overflow: hidden;
    background: var(--page-bg);
    font-family: "Lato", sans-serif;
  }
  .canvas {
    position: relative;
    width: 1200px;
    height: 800px;
  }
  .card {
    position: absolute;
    top: 250px;
    width: 525px;
    height: 300px;
    background: var(--card-white);
    border-radius: 4px;
    overflow: hidden;
    box-shadow: 0 10px 30px rgba(60, 40, 80, 0.18);
  }
  .card--front { left: 50px; }
  .card--back { left: 625px; }
  .card-shape {
    position: absolute;
    inset: 0;
    width: 100%;
    height: 100%;
  }
  .brand {
    position: absolute;
    display: flex;
    align-items: center;
    gap: 10px;
    color: var(--brand-purple);
    font-family: "Lato", sans-serif;
    font-weight: 700;
    font-size: 34px;
    letter-spacing: 0.5px;
  }
  .brand-mark {
    width: 22px;
    height: 22px;
    background: var(--brand-purple);
  }
  .card--front .brand {
    left: 0;
    right: 0;
    top: 92px;
    justify-content: center;
  }
  .name-ribbon {
    position: absolute;
    left: 150px;
    top: 182px;
    width: 225px;
    height: 28px;
    background: var(--brand-purple);
    color: var(--text-light);
    font-size: 11.5px;
    line-height: 28px;
    text-align: center;
    border-radius: 2px;
  }
  .card--back .brand {
    left: 60px;
    top: 118px;
  }
  .holder {
    position: absolute;
    right: 20px;
    top: 32px;
    text-align: right;
    color: var(--text-light);
  }
  .holder-name {
    font-family: "Oswald", sans-serif;
    font-weight: 600;
    font-size: 25px;
    text-transform: uppercase;
    line-height: 1.1;
    white-space: nowrap;
  }
  .holder-title {
    font-size: 10px;
    color: var(--text-muted);
    margin-top: 2px;
  }
  .icon-tab {
    position: absolute;
    left: 288px;
    top: 110px;
    width: 30px;
    height: 84px;
    background: var(--brand-purple);
    border-radius: 3px;
    display: flex;
    flex-direction: column;
    justify-content: space-evenly;
    align-items: center;
  }
  .icon-tab svg { width: 12px; height: 12px; fill: var(--text-light); }
  .contact-list {
    position: absolute;
    left: 330px;
    top: 114px;
    list-style: none;
    color: var(--text-light);
    font-size: 11.5px;
    line-height: 19px;
  }
</style>
</head>
<body>
<main class="canvas">

  <section class="card card--front" aria-label="Card front">
    <svg class="card-shape" viewBox="0 0 525 300" aria-hidden="true">
      <polygon fill="var(--panel-dark)" points="0,118 118,118 168,196 357,196 407,118 525,118 525,300 0,300"/>
    </svg>
    <div class="brand"><span class="brand-mark"></span>Larkvale</div>
    <div class="name-ribbon">Dalton Whitmore, Pharm. D President</div>
  </section>

  <section class="card card--back" aria-label="Card back">
    <svg class="card-shape" viewBox="0 0 525 300" aria-hidden="true">
      <polygon fill="var(--panel-dark)" points="296,0 525,0 525,300 180,300 180,215 296,122"/>
    </svg>
    <div class="brand"><span class="brand-mark"></span>Larkvale</div>
    <div class="holder">
      <div class="holder-name">Dalton Whitmore</div>
      <div class="holder-title">Pharm.D. President</div>
    </div>
    <div class="icon-tab" aria-hidden="true">
      <svg viewBox="0 0 24 24"><path d="M6.6 10.8a15 15 0 0 0 6.6 6.6l2.2-2.2a1 1 0 0 1 1-.25 11 11 0 0 0 3.6.6 1 1 0 0 1 1 1V20a1 1 0 0 1-1 1A17 17 0 0 1 3 4a1 1 0 0 1 1-1h3.5a1 1 0 0 1 1 1 11 11 0 0 0 .6 3.6 1 1 0 0 1-.25 1z"/></svg>
      <svg viewBox="0 0 24 24"><path d="M6.6 10.8a15 15 0 0 0 6.6 6.6l2.2-2.2a1 1 0 0 1 1-.25 11 11 0 0 0 3.6.6 1 1 0 0 1 1 1V20a1 1 0 0 1-1 1A17 17 0 0 1 3 4a1 1 0 0 1 1-1h3.5a1 1 0 0 1 1 1 11 11 0 0 0 .6 3.6 1 1 0 0 1-.25 1z"/></svg>
      <svg viewBox="0 0 24 24"><path d="M2 5h20v14H2z M3 6l9 7 9-7" stroke="#8f6bb3" stroke-width="1.5"/></svg>
      <svg viewBox="0 0 24 24"><path d="M12 3l10 9h-3v9h-5v-6h-4v6H5v-9H2z"/></svg>
    </div>
    <ul class="contact-list">
      <li>+ 555-014-2871</li>
      <li>+ 555-017-3390</li>
      <li>d.whitmore@larkvale.co</li>
      <li>Do you want an address?</li>
    </ul>
  </section>

</main>
</body>
</html>
```